Christmas Party Poster

I am promoting a Christmas Party for teenagers age 13-17 years old. The event is the first of its kind in our area, Weston Super Mare. The ticket price is to include food, soft drink's, music, entertainment.

There is nothing else of its kind in the the area or surrounding towns so a one of a kind event and new to the town. I would like the poster to be as simple and less busy as possible while still clearly showing the key information, anything that can be added it to show its a Christmas party for teenagers would be great. Also this is aimed at 13-17 year old's so as current and modern a design as possible.
Updates

A big thank you for the designs so far, As this is my first project I'm just getting the hang of what to ask for. I have slightly updated the brief and I now realize less is more, so long as the poster has the key elements of event name, date, time's, location, price and age range. The rest I should have been more flexible on. Thank you for your patience.

Target Market(s)

My Target Market are teenagers specifically 13-17 year olds

Industry/Entity Type

Town

Requirements
Must have
• The Title 'Frostlark' The venue is 'The Amber Pavilion w-s-m', Phone Number '01934 582093' Date '19th December'. Times '19.00 - 23.00'. Strictly u18 or age 13-17 years. Ticket price of £20. Face book 'frost lark wsm' limited 4 tickets per person
Nice to have
• Christmas Party, Photo of your night out. Food and drink included
Should not have
• no worded reference to Santa, snowmen, reindeer, disco, try to keep out as not to offend cool teenagers.

```html
<!DOCTYPE html>
<html lang="en">
<head>
<meta charset="UTF-8">
<title>Frostlark Christmas Party</title>
<link href="https://fonts.googleapis.com/css2?family=Luckiest+Guy&family=Open+Sans:wght@400&family=Roboto+Condensed:wght@400&display=swap" rel="stylesheet">
<style>
  :root {
    --stage: #000000;
    --red-deep: #c40f17;
    --red-mid: #e0202a;
    --red-light: #f25a5e;
    --white: #ffffff;
    --ink: #111111;
    --venue-blue: #1763d6;
    --date-red: #e2141c;
    --balloon-green: #3fae6a;
    --balloon-pink: #d0458f;
    --balloon-blue: #3a62c4;
    --balloon-orange: #f08a3a;
    --skin: #e9b48f;
    --dress: #d5141b;
    --gift-lilac: #b48ad6;
    --gift-magenta: #c2337f;
  }
  * { margin: 0; padding: 0; box-sizing: border-box; }
  html, body {
    width: 1200px; height: 900px; overflow: hidden;
    background: var(--stage);
  }
  .poster {
    position: absolute; left: 310px; top: 0;
    width: 580px; height: 900px; overflow: hidden;
    background:
      radial-gradient(ellipse 60% 35% at 30% 62%, var(--red-light), transparent 70%),
      linear-gradient(180deg, var(--red-deep) 0%, var(--red-mid) 55%, var(--red-deep) 100%);
  }
  .layer { position: absolute; left: 0; top: 0; width: 580px; height: 900px; }
  .balloons {
    position: absolute; left: 0; top: 0; width: 580px; height: 150px;
    background: linear-gradient(90deg,
      var(--balloon-pink) 0%, var(--balloon-green) 20%, var(--balloon-blue) 40%,
      var(--balloon-orange) 55%, var(--balloon-green) 72%, var(--balloon-blue) 86%, var(--balloon-green) 100%);
    -webkit-mask-image: linear-gradient(180deg, #000 30%, transparent 100%);
    mask-image: linear-gradient(180deg, #000 30%, transparent 100%);
    opacity: 0.75;
  }
  .model {
    position: absolute; left: 265px; top: 305px; width: 315px; height: 460px;
    background: linear-gradient(180deg, var(--dress) 0%, var(--skin) 30%, var(--dress) 60%, var(--dress) 100%);
    -webkit-mask-image: radial-gradient(ellipse 50% 50% at 55% 50%, #000 55%, transparent 100%);
    mask-image: radial-gradient(ellipse 50% 50% at 55% 50%, #000 55%, transparent 100%);
    opacity: 0.8;
  }
  .gifts {
    position: absolute; left: 255px; top: 715px; width: 325px; height: 185px;
    background: linear-gradient(120deg, var(--gift-lilac), var(--gift-magenta));
    -webkit-mask-image: radial-gradient(ellipse 55% 60% at 55% 65%, #000 50%, transparent 100%);
    mask-image: radial-gradient(ellipse 55% 60% at 55% 65%, #000 50%, transparent 100%);
  }
  .display {
    font-family: "Luckiest Guy", "Arial Black", sans-serif;
    fill: var(--white);
    stroke: var(--ink);
    stroke-width: 3px;
    paint-order: stroke fill;
    stroke-linejoin: round;
  }
  .venue { font-family: "Luckiest Guy", "Arial Black", sans-serif; fill: var(--venue-blue); }
  .when { font-family: "Open Sans", sans-serif; fill: var(--date-red); }
  .details {
    position: absolute; left: 10px; width: 360px; text-align: center;
    font-family: "Roboto Condensed", "Arial Narrow", sans-serif; color: var(--white);
    white-space: nowrap;
  }
  .tickets { top: 588px; font-size: 25px; }
  .extras { top: 632px; font-size: 27px; line-height: 1.0; text-transform: uppercase; }
  .contact {
    position: absolute; left: 33px; top: 772px;
    font-family: "Open Sans", sans-serif; font-size: 17px; color: var(--white);
  }
  .contact p { height: 31px; display: flex; align-items: center; white-space: nowrap; }
  .social-square {
    display: inline-block; width: 27px; height: 27px; margin-right: 5px;
    background: var(--white); border: 2px solid var(--ink);
  }
</style>
</head>
<body>
  <main class="poster">
    <svg class="layer" viewBox="0 0 580 900" aria-hidden="true">
      <polygon points="0,302 580,222 580,438 0,500" fill="#ffffff"/>
    </svg>
    <div class="balloons" role="img" aria-label="Cluster of colourful party balloons across the top"></div>
    <div class="model" role="img" aria-label="Photo of a young woman in a red dress and festive hat"></div>
    <div class="gifts" role="img" aria-label="Pile of wrapped presents with gold ribbons"></div>

    <svg class="layer" viewBox="0 0 580 900">
      <defs>
        <filter id="hard-shadow" x="-5%" y="-20%" width="115%" height="150%">
          <feDropShadow dx="4" dy="4" stdDeviation="0" flood-color="#111111"/>
        </filter>
      </defs>
      <g filter="url(#hard-shadow)">
        <text class="display" x="38" y="168" font-size="92" textLength="502" lengthAdjust="spacingAndGlyphs">FROSTLARK!</text>
        <text class="display" x="36" y="238" font-size="62" textLength="508" lengthAdjust="spacingAndGlyphs">CHRISTMAS PARTY!</text>
        <text class="display" x="56" y="574" font-size="38" stroke-width="2" textLength="280" lengthAdjust="spacingAndGlyphs">AGE 13-17 YEARS</text>
      </g>
      <g transform="rotate(-9.5 12 362)">
        <text class="venue" x="12" y="362" font-size="40" textLength="532" lengthAdjust="spacingAndGlyphs">THE AMBER PAVILION W-S-M</text>
      </g>
      <g transform="rotate(-7 26 420)">
        <text class="when" x="26" y="420" font-size="32">19th December</text>
        <text class="when" x="34" y="460" font-size="32">19:00-23:00</text>
      </g>
    </svg>

    <p class="details tickets">Tickets £20</p>
    <p class="details extras">Photos of your night<br>Food &amp; drink included</p>

    <div class="contact">
      <p>Phone Number #01934582093</p>
      <p><span class="social-square"></span>frost lark wsm</p>
      <p>4 Ticket limit per person</p>
    </div>
  </main>
</body>
</html>
```